amber crest health and wellness group.

need a full website design , all information provided in word document labeled website blue print

Target Market(s)

first responders, military , people in crisis

Coding

Coded - Design and coding required

Number of Pages Required

1 page

```html
<!DOCTYPE html>
<html lang="en">
<head>
<meta charset="utf-8">
<title>Amber Crest Health and Wellness Group</title>
<link href="https://fonts.googleapis.com/css2?family=Plus+Jakarta+Sans:wght@400;500;600;700;800&family=Questrial&display=swap" rel="stylesheet">
<style>
:root{
  --navy:#25558f;
  --navy-dark:#0f3153;
  --green:#6cc04a;
  --bg-soft:#f2f5f9;
  --text:#5b6470;
  --white:#ffffff;
  --line:#dfe4ea;
}
*{margin:0;padding:0;box-sizing:border-box}
html,body{width:1200px;height:2896px;overflow:hidden}
body{position:relative;font-family:"Questrial",sans-serif;color:var(--text);background:var(--white)}
.abs{position:absolute}
.head{font-family:"Plus Jakarta Sans",sans-serif}
.btn{position:absolute;display:flex;align-items:center;justify-content:center;background:var(--green);color:var(--white);font-family:"Plus Jakarta Sans",sans-serif;font-weight:700;font-size:10.5px;letter-spacing:.2px;border-radius:4px;text-transform:uppercase}
.eyebrow{font-family:"Plus Jakarta Sans",sans-serif;font-size:12.5px;text-transform:uppercase;letter-spacing:.2px;color:#7b8490}
.section-title{font-family:"Plus Jakarta Sans",sans-serif;font-weight:500;color:var(--navy);font-size:35px;line-height:38px;letter-spacing:-.8px}

/* top bar */
.topbar{left:0;top:0;width:1200px;height:27px;background:var(--navy);color:var(--white);font-family:"Plus Jakarta Sans",sans-serif;font-size:9.5px;font-weight:600}
.topbar .notice{left:122px;top:8px}
.topbar .links{right:122px;top:8px;display:flex;gap:18px}

/* nav */
.nav{left:0;top:27px;width:1200px;height:54px;background:var(--white)}
.brand{left:122px;top:27px;width:153px;height:116px;background:var(--white);z-index:3;display:flex;flex-direction:column;align-items:center;justify-content:center;gap:6px}
.brand .mark{width:20px;height:20px;border-radius:50%;background:var(--navy)}
.brand .name{font-family:"Plus Jakarta Sans",sans-serif;font-weight:700;color:var(--navy);font-size:13px;line-height:15px;text-align:center;text-transform:uppercase}
.menu{left:285px;top:48px;display:flex;gap:17px;font-family:"Plus Jakarta Sans",sans-serif;font-weight:700;font-size:10.5px;color:var(--navy)}
.signin{left:898px;top:48px;font-family:"Plus Jakarta Sans",sans-serif;font-weight:700;font-size:10.5px;color:var(--navy)}

/* hero */
.hero{left:0;top:81px;width:1200px;height:594px;background:linear-gradient(90deg,#2a2520 0%,#4a3a2c 35%,#8a6a50 60%,#a8815f 80%,#6a5038 100%)}
.hero-shade{left:0;top:81px;width:1200px;height:594px;background:linear-gradient(90deg,rgba(20,18,16,.55),rgba(20,18,16,0) 60%)}
.hero .eyebrow,.hero-copy .eyebrow{color:#e8e1d8}
.hero-copy{left:122px;top:266px;width:600px;color:var(--white)}
.hero-copy h1{font-family:"Plus Jakarta Sans",sans-serif;font-weight:500;font-size:59px;line-height:64px;letter-spacing:-1.8px;margin-top:8px}
.hero-copy p{font-size:12.5px;line-height:19px;width:540px;margin-top:14px}

/* who we serve */
.serve{left:0;top:675px;width:1200px;height:463px;background:var(--bg-soft)}
.center{left:0;width:1200px;text-align:center}
.card{position:absolute;top:835px;width:225px;height:253px;background:var(--white);border-radius:8px;padding:18px 17px}
.card svg{display:block}
.card h3{font-family:"Plus Jakarta Sans",sans-serif;font-weight:500;color:var(--navy);font-size:18.5px;line-height:22px;letter-spacing:-.4px;margin-top:48px}
.card p{font-size:12px;line-height:19px;margin-top:14px}

/* about */
.about-copy{left:122px;top:1202px;width:420px}
.about-copy .section-title{margin-top:6px}
.about-copy .intro{font-size:12.5px;line-height:19px;margin-top:20px;width:405px}
.divider{position:absolute;left:122px;width:406px;height:1px;background:var(--line)}
.mission{position:absolute;left:122px;width:406px}
.mission .dot{position:absolute;left:2px;top:9px;width:20px;height:20px;border-radius:50%;background:#9aa3ad}
.mission h4{position:absolute;left:32px;top:0;font-family:"Plus Jakarta Sans",sans-serif;font-weight:500;color:var(--navy);font-size:22px;letter-spacing:-.5px}
.mission p{position:absolute;left:32px;top:32px;width:250px;font-size:11px;line-height:17px}
.about-photo{left:591px;top:1218px;width:487px;height:411px;border-radius:10px;background:linear-gradient(135deg,#d9cfc2 0%,#c9b9a6 30%,#4a86c2 55%,#9cc6dd 80%,#e9e4dd 100%)}

/* services */
.services{left:0;top:1679px;width:1200px;height:514px;background:var(--bg-soft)}
.svc{position:absolute;top:1802px;width:306px;height:275px;background:var(--white);border-radius:8px;overflow:hidden}
.svc .photo{height:203px}
.svc h3{position:absolute;left:17px;top:203px;height:72px;width:220px;display:flex;align-items:center;font-family:"Plus Jakarta Sans",sans-serif;font-weight:500;color:var(--navy);font-size:18.5px;line-height:22px;letter-spacing:-.4px}
.svc .plus{position:absolute;right:17px;top:221px;width:36px;height:36px;border-radius:4px;background:var(--bg-soft);color:var(--navy);font-size:20px;font-weight:700;display:flex;align-items:center;justify-content:center;font-family:"Plus Jakarta Sans",sans-serif}

/* cta */
.cta{left:0;top:2193px;width:1200px;height:413px;background:linear-gradient(90deg,#0f3153 0%,#143a5e 35%,#3b4a4a 55%,#5d5446 70%,#c9ced2 85%,#a9aeb2 100%)}
.cta-copy{left:122px;top:2292px;width:420px;color:var(--white)}
.cta-copy h2{font-family:"Plus Jakarta Sans",sans-serif;font-weight:500;font-size:35px;line-height:38px;letter-spacing:-.8px}
.cta-copy .kicker{font-family:"Plus Jakarta Sans",sans-serif;font-weight:800;color:var(--green);font-size:16px;letter-spacing:1px;text-transform:uppercase;margin-top:2px}
.cta-copy p{font-size:12.5px;line-height:19px;margin-top:14px}

/* footer */
.footer{left:0;top:2606px;width:1200px;height:290px;background:var(--bg-soft)}
.fcol{position:absolute;top:2640px}
.fcol h5{font-family:"Plus Jakarta Sans",sans-serif;font-weight:700;color:var(--navy);font-size:12.5px;line-height:14px;text-transform:uppercase}
.fcol ul{list-style:none;margin-top:14px}
.fcol li{font-size:11px;line-height:21px;color:var(--text)}
.contact-row{display:flex;gap:7px;font-size:11px;line-height:16px;margin-top:14px}
.contact-row svg{flex:none;margin-top:2px}
.member{left:122px;top:2736px}
.member h5{font-family:"Plus Jakarta Sans",sans-serif;font-weight:700;color:var(--navy);font-size:12.5px;text-transform:uppercase}
.member p{font-size:10.5px;margin-top:6px;color:var(--text)}
.member u{font-weight:700}
.foot-line{left:122px;top:2825px;width:956px;height:1px;background:var(--line)}
.copyright{left:122px;top:2856px;font-size:10.5px}
.socials{left:518px;top:2843px;display:flex;gap:7px}
.socials span{width:36px;height:36px;border-radius:50%;border:1px solid #9db1c9}
.legal{right:122px;top:2856px;display:flex;gap:9px;font-size:10.5px}
</style>
</head>
<body>

<div class="abs topbar">
  <span class="abs notice">IS YOUR STATE READY FOR RURAL HEALTH TRANSFORMATION?</span>
  <div class="abs links"><span>HEALTH PLANS</span><span>GOVERNMENTS</span><span>SUCCESS STORIES</span><span>SUPPORT</span></div>
</div>

<div class="abs nav"></div>
<div class="abs brand">
  <span class="mark"></span>
  <span class="name">Amber Crest<br>Health &amp; Wellness Group</span>
</div>
<nav class="abs menu"><span>HOME</span><span>ABOUT US</span><span>OUR SERVICES</span><span>OUR TEAM</span><span>FAQS</span><span>CONTACT US</span></nav>
<span class="abs signin">SIGN IN</span>
<span class="btn" style="left:950px;top:40px;width:72px;height:29px">SIGN UP</span>
<svg class="abs" style="left:1035px;top:48px" width="13" height="13" viewBox="0 0 13 13" fill="none" stroke="#25558f" stroke-width="1.6"><circle cx="5.5" cy="5.5" r="4.2"/><path d="M8.6 8.6L12 12"/></svg>
<svg class="abs" style="left:1059px;top:47px" width="19" height="14" viewBox="0 0 19 14" stroke="#25558f" stroke-width="1.6"><path d="M0 1h19M5 7h14M0 13h19"/></svg>

<div class="abs hero" role="img" aria-label="Photo of a woman warmly embracing another person in a caring hug"></div>
<div class="abs hero-shade"></div>
<div class="abs hero-copy">
  <div class="eyebrow">Trauma-Informed &amp; Compassionate</div>
  <h1>Helping Those Who<br>Help Others</h1>
  <p>Supporting the mental health professionals, caregivers, and community leaders who dedicate their lives to the well-being of others.</p>
</div>
<span class="btn" style="left:122px;top:472px;width:185px;height:41px">Request a Consultation</span>

<div class="abs serve"></div>
<div class="abs center eyebrow" style="top:723px">Who We Serve</div>
<h2 class="abs center section-title" style="top:741px">Supporting The Individuals and Team<br>Dedicated To Caring</h2>

<div class="card" style="left:122px">
  <svg width="46" height="46" viewBox="0 0 46 46" fill="none" stroke="#25558f" stroke-width="2"><path d="M8 10c-6 8-4 22 10 30l5-5-6-6-4 3c-3-4-4-8-3-12l5-1-1-8z"/><circle cx="26" cy="18" r="10"/><text x="20" y="22" font-size="10" fill="#25558f" stroke="none" font-family="sans-serif" font-weight="700">24</text><path d="M38 4v8M34 8h8" stroke="#6cc04a"/></svg>
  <h3>First Responders and Frontline Workers</h3>
  <p>First responders are specially trained professionals who are the first to arrive at emergencies, providing immediate help.</p>
</div>
<div class="card" style="left:366px">
  <svg width="50" height="46" viewBox="0 0 50 46" fill="none" stroke="#25558f" stroke-width="2"><rect x="2" y="20" width="46" height="24" rx="2"/><path d="M2 28h46M25 20V6h14v8M25 34v4"/><rect x="8" y="12" width="10" height="8" stroke="#6cc04a"/></svg>
  <h3>Agencies and All Types of Institutions</h3>
  <p>Mental health care involves a diverse ecosystem of government agencies, specialized Central &amp; State Institutions programs.</p>
</div>
<div class="card" style="left:610px">
  <svg width="44" height="46" viewBox="0 0 44 46" fill="none" stroke="#25558f" stroke-width="2"><circle cx="22" cy="12" r="8"/><path d="M4 44c0-12 8-18 18-18s18 6 18 18zM14 28v10M30 28v6"/><circle cx="30" cy="37" r="3" stroke="#6cc04a"/></svg>
  <h3>For Mental Health Clinicians</h3>
  <p>Looking for reflective, trauma-in-formed support to strengthen their practice and sense of professional stability.</p>
</div>
<div class="card" style="left:853px">
  <svg width="36" height="48" viewBox="0 0 36 48" fill="none" stroke="#25558f" stroke-width="2"><rect x="2" y="2" width="32" height="44" rx="4"/><rect x="9" y="10" width="18" height="10" rx="2"/><path d="M14 26h8v8l-4 4-4-4z" stroke="#6cc04a"/></svg>
  <h3>Armed Forces and Mental Health</h3>
  <p>Working in stressful and traumatic situations military personnel and veterans can face unique risks and challenges to their mental health.</p>
</div>

<div class="abs about-copy">
  <div class="eyebrow">Effective Care Begins With Caring</div>
  <h2 class="section-title">About Amber Crest Health and Wellness Group</h2>
  <p class="intro">Lorem ipsum dolor sit amet, consectetur adipiscing elit, sed do eiusmod tempor incididunt ut labore et dolore magna aliqua. Ut enim ad minim veniam, quis nostrud exercitation ullamco laboris nisi ut ali quip ex ea commodo consequat.</p>
</div>
<div class="divider" style="top:1408px"></div>
<div class="mission" style="top:1420px">
  <span class="dot"></span>
  <h4>Our Mission</h4>
  <p>Lorem ipsum dolor sit amet, consectetur adipiscing elit, sed do eiusmod tempor incididunt ut labore et dolore magna aliqua.</p>
</div>
<span class="btn" style="left:412px;top:1462px;width:116px;height:41px">Learn More</span>
<div class="divider" style="top:1521px"></div>
<div class="mission" style="top:1533px">
  <span class="dot"></span>
  <h4>Our Mission</h4>
  <p>Lorem ipsum dolor sit amet, consectetur adipiscing elit, sed do eiusmod tempor incididunt ut labore et dolore magna aliqua.</p>
</div>
<span class="btn" style="left:412px;top:1575px;width:116px;height:41px">Learn More</span>
<div class="abs about-photo" role="img" aria-label="Photo of a smiling nurse in blue scrubs holding hands with an elderly patient"></div>

<div class="abs services"></div>
<div class="abs center eyebrow" style="top:1727px">Providing A Wide Range Services</div>
<h2 class="abs center section-title" style="top:1745px">Designed To Promote Healing, Growth</h2>

<div class="svc" style="left:122px">
  <div class="photo" role="img" aria-label="Photo of a counsellor talking with a client in a bright office" style="background:linear-gradient(135deg,#d8d4cc,#8a8f95 55%,#3f4a57)"></div>
  <h3>Mental Health Therapy</h3><span class="plus">+</span>
</div>
<div class="svc" style="left:447px">
  <div class="photo" role="img" aria-label="Photo of two responders in red vests helping an injured worker on a site" style="background:linear-gradient(135deg,#6b5a48,#b07a4a 45%,#c2413a 60%,#4b4f55)"></div>
  <h3>Trauma &amp; First Responder Support</h3><span class="plus">+</span>
</div>
<div class="svc" style="left:772px">
  <div class="photo" role="img" aria-label="Photo of glowing pink salt crystals in a wooden salt therapy room" style="background:radial-gradient(ellipse at 55% 55%,#f7b89a,#e0826a 45%,#b88a62 80%,#9a7352)"></div>
  <h3>Salt Therapy (Halotherapy)</h3><span class="plus">+</span>
</div>
<div class="svc" style="left:1097px">
  <div class="photo" role="img" aria-label="Photo of a sound healing session with people resting" style="background:linear-gradient(135deg,#5a4a40,#9b8cb0 50%,#c9b8a6)"></div>
  <h3>Sound &amp; Vibration</h3><span class="plus">+</span>
</div>
<span class="btn" style="left:508px;top:2102px;width:185px;height:41px">View All Services</span>

<div class="abs cta" role="img" aria-label="Photo of a clinician in conversation with a client during a counselling session"></div>
<div class="abs cta-copy">
  <h2>Let’s See The Impact Of Better Mental Health</h2>
  <div class="kicker">Ready To Take The Next Step?</div>
  <p>Whether you’re a clinician, a leader, or a community organization, we’re here to help you flourish.</p>
</div>
<span class="btn" style="left:122px;top:2481px;width:185px;height:41px">Request a Consultation</span>

<footer class="abs footer"></footer>
<div class="fcol" style="left:122px"><h5>Want To Join Our<br>Provider Network?</h5></div>
<span class="btn" style="left:122px;top:2680px;width:117px;height:41px">Apply To Join</span>
<div class="abs member"><h5>Already A Member?</h5><p><u>Sign In</u> or <u>Sign up</u></p></div>

<div class="fcol" style="left:366px"><h5>Quick Links</h5><ul><li>Home</li><li>About Us</li><li>Who We Serve</li><li>FAQs</li><li>Trust &amp; Security</li><li>Contact Us</li></ul></div>
<div class="fcol" style="left:503px"><h5>Why Amber Crest</h5><ul><li>Our Impact</li><li>Our Customers</li><li>Our Methodology</li><li>Our Care Network</li><li>Our Technology</li></ul></div>
<div class="fcol" style="left:663px"><h5>Resources</h5><ul><li>Blog</li><li>Case Studies</li><li>Research, Guides, &amp; Assessments</li><li>Events &amp; Webinars</li><li>For Health Plans</li></ul></div>
<div class="fcol" style="left:863px;width:215px">
  <h5>Contact Us</h5>
  <div class="contact-row"><svg width="10" height="12" viewBox="0 0 10 12"><path d="M5 0a4.5 4.5 0 0 0-4.5 4.5C.5 8 5 12 5 12s4.5-4 4.5-7.5A4.5 4.5 0 0 0 5 0z" fill="#6cc04a"/><circle cx="5" cy="4.5" r="1.6" fill="#fff"/></svg><span>Address: Harbourview Plaza, 218 Linden Ave, Brookfield, ON L0R 1X2, Canada</span></div>
  <div class="contact-row" style="margin-top:26px"><svg width="11" height="11" viewBox="0 0 11 11"><path d="M2 0l2 3-1 1.5c.8 1.5 2 2.7 3.5 3.5L8 7l3 2-1 2C5 11 0 6 0 1z" fill="#6cc04a"/></svg><span>Phone: 555-204-3187</span></div>
  <div class="contact-row" style="margin-top:20px"><svg width="12" height="9" viewBox="0 0 12 9"><rect width="12" height="9" rx="1" fill="#6cc04a"/><path d="M0.5 0.8L6 5l5.5-4.2" stroke="#fff" fill="none"/></svg><span>Email: hello@ambercresthealth.com</span></div>
</div>

<div class="abs foot-line"></div>
<div class="abs copyright">©2025 Amber Crest Health And Wellness Group. All Rights Reserved.</div>
<div class="abs socials"><span></span><span></span><span></span><span></span></div>
<div class="abs legal"><span>Terms of Use</span><span>Privacy Policy</span><span>CA Privacy Notice</span><span>Formal Complaint</span></div>

</body>
</html>
```